Keep Tomorrow Book Cover

I am looking for book front cover ideas. The book trim size will be 5.5 x 8.5 in so please make the mock up that size. The book Title is "Keep Tomorrow" and the Subtitle is "Counsel for the Crossroads Nobody Warns You About". The audience for the book is leaders in high-growth companies. It consists of a series of letters and advice for specific problems the leader will encounter on their journey. The design needs to be attractive to both male and female readers. I am attaching a file with brand colors and some rough ideas that need to be refined. The examples lean toward a feminine vibe but I want the cover to be more universal. Please use the brand colors identified in the file.

```html
<!DOCTYPE html>
<html lang="en">
<head>
<meta charset="UTF-8">
<title>Keep Tomorrow – Book Cover</title>
<link rel="stylesheet" href="https://fonts.googleapis.com/css2?family=Old+Standard+TT:wght@700&family=Heebo:wght@500;600&display=swap">
<style>
  :root {
    --page: #ffffff;
    --sage: #b0bda8;
    --ink: #0b0b0b;
    --tan: #b3865a;
    --envelope: #c69c6b;
    --cream: #f4e8d4;
    --leaf-dark: #373a3c;
    --leaf-green: #687a60;
    --leaf-olive: #9b965e;
    --leaf-gold: #d3ad6a;
  }
  * { margin: 0; padding: 0; box-sizing: border-box; }
  html, body {
    width: 1200px;
    height: 1200px;
    overflow: hidden;
    background: var(--page);
  }
  .canvas {
    position: relative;
    width: 1200px;
    height: 1200px;
  }
  .book-cover {
    position: absolute;
    left: 221px;
    top: 31px;
    width: 758px;
    height: 1137px;
    background: var(--sage);
  }
  .cover-title {
    position: absolute;
    top: 86px;
    left: 0;
    width: 100%;
    text-align: center;
    font-family: "Old Standard TT", "Times New Roman", serif;
    font-weight: 700;
    font-size: 70px;
    line-height: 1;
    letter-spacing: 0;
    color: var(--ink);
    text-transform: uppercase;
    white-space: nowrap;
  }
  .cover-subtitle {
    position: absolute;
    top: 194px;
    left: 0;
    width: 100%;
    text-align: center;
    font-family: "Heebo", "Helvetica Neue", Arial, sans-serif;
    font-weight: 500;
    font-size: 30px;
    line-height: 37px;
    letter-spacing: 1px;
    color: var(--tan);
    text-transform: uppercase;
  }
  .cover-illustration {
    position: absolute;
    left: 125px;
    top: 307px;
    width: 506px;
    height: 655px;
  }
  .cover-author {
    position: absolute;
    top: 1056px;
    left: 0;
    width: 100%;
    text-align: center;
    font-family: "Heebo", "Helvetica Neue", Arial, sans-serif;
    font-weight: 600;
    font-size: 39px;
    line-height: 1;
    letter-spacing: 1.5px;
    color: var(--tan);
    text-transform: uppercase;
  }
</style>
</head>
<body>
  <div class="canvas">
    <div class="book-cover">
      <h1 class="cover-title">Keep Tomorrow</h1>
      <p class="cover-subtitle">Counsel for the Crossroads<br>Nobody Warns You About</p>
      <svg class="cover-illustration" viewBox="0 0 506 655" role="img"
           aria-label="Illustration of an open envelope with a tree of dark, green and golden leaves growing out of it">
        <defs>
          <radialGradient id="illustrationTone" cx="0.5" cy="0.3" r="0.75">
            <stop offset="0" stop-color="var(--leaf-dark)"/>
            <stop offset="0.35" stop-color="var(--leaf-green)"/>
            <stop offset="0.6" stop-color="var(--leaf-gold)"/>
            <stop offset="0.8" stop-color="var(--cream)"/>
            <stop offset="1" stop-color="var(--envelope)"/>
          </radialGradient>
        </defs>
        <rect x="0" y="0" width="506" height="655" rx="18" fill="url(#illustrationTone)"/>
      </svg>
      <p class="cover-author">Daria Wellsford Lane</p>
    </div>
  </div>
</body>
</html>
```